Pharmacy handmade, Personalized Medical Cosmetics Label

Medical Cosmetics label, elegant and professional looking. The creams are Dermatologist formulated and are prepared by local Pharmacy. The label should be versatile and allow space for hand writing to be filled by the pharmacist preparing the product.
The following information will be handwritten:
Upper lid - Lid Balm No.5 ; Marigold, Retinol ; 30
Lower Bottom - Teodora Halvik ; Signature ; 01.01.2017
Upper Lid Label
Velluto Skin (logo)
Clinic Remedy
(circular pattern - Doctor Formulated, Registered Pharmacy, Handmade, Highest Medical Standards)
(Lid Balm No.5 - in hand writing and different color, maybe red)
Key Ingredients: (Marigold, Retinol - in hand writing, same color as above, maybe red)
(box with hand writing 30) ml
Lower Bottom Label (underneath surface of the container)
Made for Velluto Skin by
Pharmacy Lorant, 7 Pelister blvd., Sofia, ph. 0893517460
Patient: (Teodora Halvik- in hand writing)
Pharmacist: (Signature - in hand writing)
Date: (01.01.2017 - in hand writing)
For External Use
good for 60 days after preparation
Ingredients: Retinol, Marigold Extract, Water, Glycerin, Stearyl Alcohol, Wheat Germ Oil, Polysorbate 60, Sesame Oil, Myristyl Myristate, Cetyl Alcohol, Sorbitan Stearate, Phenoxyethanol, Calendula Extract, Cornflower Extract, Sodium Alginate, Sodium Citrate.
The container lid and bottom are 5 cm = 50 mm in diameter. Made from aluminum and contain 30ml or 50ml.
Please refer to the screen shots from my Web Site to get the feeling for the color pallet and professional look. These creams will be sold on this website. They are custom made by a registered Pharmacy right on the spot after the order has been placed. This is why I need more space for the hand written notes made by the pharmacist who prepared the order.
Please make the design professional, simple and serious colors, like light brown, beige, black or dark brown letters, red hand writing (will be filled by pen or thin marker by the Pharmacist by hand, depending on the order, patient name, etc.)
Thank you.
female 24 - 49 year old
Medical

```html
<!DOCTYPE html>
<html lang="en">
<head>
<meta charset="utf-8">
<title>Velluto Skin – Clinic Remedy Labels</title>
<link rel="stylesheet" href="https://fonts.googleapis.com/css2?family=Raleway:wght@500;700;800&family=Lora:wght@400&family=Quicksand:wght@400&family=Rouge+Script&display=swap">
<style>
  :root {
    --stage: #dcdcdc;
    --rim: #ffffff;
    --rim-line: #b9b9b9;
    --label-beige: #e6e3d3;
    --field-white: #fbfbf8;
    --mauve: #7a6470;
    --mauve-text: #6e5f66;
    --logo-blue: #6f8a99;
    --ink-red: #b0302a;
    --rule: #8e7f86;
    --body-grey: #77766c;
    --ring-text: #6a6a6a;
  }
  * { margin: 0; padding: 0; box-sizing: border-box; }
  html, body { width: 1200px; height: 820px; overflow: hidden; }
  body {
    background: linear-gradient(180deg, #ffffff 0%, var(--stage) 100%);
    position: relative;
  }
  .label { position: absolute; top: 160px; width: 500px; height: 500px; }
  .label--bottom { left: 80px; }
  .label--lid { left: 620px; }
  .ring-text { font-family: "Quicksand", sans-serif; font-size: 22px; letter-spacing: 3px; fill: var(--ring-text); }
  .ring-text--long { letter-spacing: 1.5px; font-size: 20px; }
  .logo-name { font-family: "Lora", serif; font-size: 32px; fill: var(--logo-blue); }
  .series-title { font-family: "Raleway", sans-serif; font-weight: 800; font-size: 66px; fill: var(--mauve); }
  .section-head { font-family: "Raleway", sans-serif; font-weight: 700; font-size: 26px; fill: var(--mauve); }
  .handwriting { font-family: "Rouge Script", cursive; fill: var(--ink-red); }
  .maker { font-family: "Raleway", sans-serif; font-size: 15px; fill: var(--body-grey); }
  .maker-strong { font-weight: 700; }
  .field-label { font-family: "Raleway", sans-serif; font-weight: 700; font-size: 15px; fill: var(--mauve-text); }
  .usage-note { font-family: "Raleway", sans-serif; font-weight: 700; font-size: 14.5px; fill: var(--mauve-text); }
  .ingredients { font-family: "Raleway", sans-serif; font-weight: 500; font-size: 15.5px; fill: var(--body-grey); }
  .ingredients-head { font-weight: 700; }
</style>
</head>
<body>

<svg class="label label--bottom" viewBox="0 0 500 500" aria-label="Underside label">
  <defs>
    <clipPath id="bottom-disc"><circle cx="250" cy="250" r="238"/></clipPath>
  </defs>
  <circle cx="250" cy="250" r="246" fill="var(--rim)" stroke="var(--rim-line)" stroke-width="2"/>
  <circle cx="250" cy="250" r="238" fill="var(--label-beige)"/>

  <g text-anchor="middle">
    <text class="maker maker-strong" x="250" y="52">Made for</text>
    <text class="maker maker-strong" x="250" y="70">Velluto Skin by:</text>
    <text class="maker" x="250" y="88">Pharmacy Lorant,</text>
    <text class="maker" x="250" y="106">7 Pelister blvd., Sofia, ph. 0893517460</text>
  </g>

  <g clip-path="url(#bottom-disc)">
    <rect x="0" y="118" width="500" height="130" fill="var(--field-white)"/>
    <rect x="0" y="258" width="500" height="30" fill="var(--field-white)"/>
  </g>

  <g class="record-fields">
    <text class="field-label" x="64" y="158">PATIENT:</text>
    <text class="handwriting" x="140" y="156" font-size="36">Teodora Halvik</text>
    <line x1="30" y1="166" x2="470" y2="166" stroke="var(--rule)" stroke-width="1.5"/>

    <text class="field-label" x="30" y="202">PHARMACIST:</text>
    <text class="handwriting" x="146" y="200" font-size="36">Elin Varsky</text>
    <line x1="22" y1="210" x2="478" y2="210" stroke="var(--rule)" stroke-width="1.5"/>

    <text class="field-label" x="96" y="240">DATE:</text>
    <text class="handwriting" x="150" y="238" font-size="36">1.01.2017</text>
  </g>

  <text class="usage-note" x="250" y="278" text-anchor="middle">FOR EXTERNAL USE: GOOD 60 DAYS AFTER PREPARATION</text>

  <g class="ingredients" text-anchor="middle">
    <text x="250" y="316"><tspan class="ingredients-head">Ingredients:</tspan> Retinol, Marigold Extract, Water,</text>
    <text x="250" y="337">Glycerin, Stearyl Alcohol, Wheat Germ Oil,</text>
    <text x="250" y="358">Polysorbate 60, Sesame Oil, Myristyl</text>
    <text x="250" y="379">Myristate, Cetyl Alcohol, Sorbitan Stearate,</text>
    <text x="250" y="400">Phenoxyethanol, Calendula Extract,</text>
    <text x="250" y="421">Cornflower Extract, Sodium</text>
    <text x="250" y="442">Alginate, Sodium Citrate.</text>
  </g>
</svg>

<svg class="label label--lid" viewBox="0 0 500 500" aria-label="Lid label">
  <defs>
    <path id="ring-path" d="M 93,407 A 222,222 0 1,1 407,93 A 222,222 0 1,1 93,407"/>
    <clipPath id="lid-disc"><circle cx="250" cy="250" r="212"/></clipPath>
  </defs>
  <circle cx="250" cy="250" r="246" fill="var(--rim)" stroke="var(--rim-line)" stroke-width="2"/>
  <circle cx="250" cy="250" r="240" fill="none" stroke="var(--rim-line)" stroke-width="1"/>
  <circle cx="250" cy="250" r="214" fill="none" stroke="var(--rim-line)" stroke-width="1"/>

  <g class="ring-text" text-anchor="middle">
    <text class="ring-text ring-text--long"><textPath href="#ring-path" startOffset="12.5%">Highest Medical Standards</textPath></text>
    <text class="ring-text"><textPath href="#ring-path" startOffset="37.5%">Doctor Formulated</textPath></text>
    <text class="ring-text"><textPath href="#ring-path" startOffset="62.5%">Registered Pharmacy</textPath></text>
    <text class="ring-text"><textPath href="#ring-path" startOffset="87.5%">Handmade</textPath></text>
  </g>

  <circle cx="250" cy="250" r="212" fill="var(--label-beige)"/>

  <text class="logo-name" x="250" y="112" text-anchor="middle">Velluto Skin</text>

  <g clip-path="url(#lid-disc)">
    <rect x="20" y="130" width="72" height="116" fill="var(--mauve)"/>
    <rect x="408" y="130" width="72" height="116" fill="var(--mauve)"/>
    <rect x="20" y="326" width="70" height="14" fill="var(--mauve)"/>
    <rect x="410" y="326" width="70" height="14" fill="var(--mauve)"/>
  </g>

  <g text-anchor="middle">
    <text class="series-title" x="250" y="184">CLINIC</text>
    <text class="series-title" x="250" y="244">REMEDY</text>
  </g>

  <text class="handwriting" x="250" y="296" font-size="50" text-anchor="middle">Lid Balm No.5</text>
  <line x1="58" y1="306" x2="442" y2="306" stroke="var(--rule)" stroke-width="1.5"/>

  <text class="section-head" x="250" y="342" text-anchor="middle">KEY INGREDIENTS</text>

  <g text-anchor="middle">
    <text class="handwriting" x="250" y="376" font-size="32">Marigold,</text>
    <line x1="74" y1="384" x2="426" y2="384" stroke="var(--rule)" stroke-width="1.5"/>
    <text class="handwriting" x="250" y="413" font-size="32">Retinol</text>
    <line x1="96" y1="421" x2="404" y2="421" stroke="var(--rule)" stroke-width="1.5"/>
    <text class="handwriting" x="250" y="450" font-size="28">30 ml</text>
  </g>
</svg>

</body>
</html>
```